Corvane Industries business cards

We need business cards for our company Corvane Industries, based in Brisbane but trading world wide. We buy and sell Corvane Industries, generators and marine equipment. The design needs to be kept clean, simple but eye catching.
Please keep with our current logo (included) and further information can be included on request

Business

0792cd
33a6d7
85cae6
3276b5
0455a3
cedeed
cee9f5
ffffff

```html
<!DOCTYPE html>
<html lang="en">
<head>
<meta charset="utf-8">
<title>Corvane Industries business cards</title>
<link rel="stylesheet" href="https://fonts.googleapis.com/css2?family=Exo+2:wght@400;500;600&display=swap">
<style>
  :root {
    --backdrop: #9b9c9e;
    --card: #ffffff;
    --brand-blue: #4485c2;
    --line-blue: #3276b5;
    --ink: #2a2a2a;
    --pill-dark: #3a3a3a;
    --pill-mid: #6a6a6a;
  }
  * { box-sizing: border-box; margin: 0; padding: 0; }
  html, body {
    width: 1200px; height: 894px; overflow: hidden;
    background: var(--backdrop);
    font-family: "Exo 2", sans-serif;
  }
  .sheet {
    width: 1200px; height: 894px;
    display: flex; align-items: center; justify-content: center; gap: 30px;
  }
  .card {
    position: relative; width: 556px; height: 318px;
    background: var(--card); overflow: hidden;
    box-shadow: 0 6px 18px rgba(0,0,0,.25);
  }

  /* Front */
  .brand { position: absolute; left: 70px; top: 52px; display: flex; align-items: center; gap: 16px; }
  .brand-square { width: 62px; height: 62px; background: var(--brand-blue); border-radius: 6px; }
  .brand-name { color: var(--brand-blue); font-size: 32px; font-weight: 500; line-height: 1; }
  .front-band {
    position: absolute; right: 0; top: 172px; width: 290px; height: 76px;
    background: var(--brand-blue); border-radius: 38px 0 0 38px;
  }

  /* Back */
  .holder { position: absolute; left: 40px; top: 34px; }
  .holder-name { color: var(--brand-blue); font-size: 24px; font-weight: 500; line-height: 1.1; }
  .holder-role { color: var(--ink); font-size: 10px; letter-spacing: .06em; text-transform: uppercase; margin-top: 2px; }
  .rule { position: absolute; height: 2px; background: var(--line-blue); }
  .rule-top { left: 40px; top: 90px; width: 300px; }
  .rule-mid { left: 20px; top: 210px; width: 330px; }
  .rule-low { left: 20px; top: 262px; width: 536px; }
  .rule-base { left: 20px; top: 292px; width: 536px; }
  .contacts { position: absolute; left: 40px; top: 104px; display: grid; grid-template-columns: 78px auto; row-gap: 4px; font-size: 15px; }
  .contacts dt { color: var(--brand-blue); }
  .contacts dd { color: var(--ink); font-weight: 500; }
  .address { position: absolute; left: 28px; top: 226px; display: flex; align-items: center; gap: 10px; color: var(--ink); font-size: 15px; font-weight: 500; }
  .back-pill {
    position: absolute; right: 0; top: 118px; width: 150px; height: 84px;
    border-radius: 42px 0 0 42px;
    background: radial-gradient(circle at 40% 50%, var(--pill-mid), var(--pill-dark) 70%);
  }
</style>
</head>
<body>
<main class="sheet">
  <section class="card card-front">
    <div class="brand">
      <span class="brand-square"></span>
      <span class="brand-name">Corvane Industries</span>
    </div>
    <div class="front-band"></div>
  </section>

  <section class="card card-back">
    <div class="holder">
      <p class="holder-name">Mara Ellison</p>
      <p class="holder-role">General Manager</p>
    </div>
    <div class="rule rule-top"></div>
    <dl class="contacts">
      <dt>Phone:</dt><dd>07 3184 2270</dd>
      <dt>Fax:</dt><dd>07 3184 2271</dd>
      <dt>Email:</dt><dd>mara@corvane.example</dd>
      <dt>website:</dt><dd>www.corvane.example</dd>
    </dl>
    <div class="rule rule-mid"></div>
    <p class="address">
      <svg width="14" height="20" viewBox="0 0 14 20" aria-hidden="true">
        <path d="M7 0C3.1 0 0 3.1 0 7c0 5 7 13 7 13s7-8 7-13c0-3.9-3.1-7-7-7z" fill="var(--line-blue)"/>
        <circle cx="7" cy="7" r="2.6" fill="#fff"/>
      </svg>
      41 Quayside Drive, Brisbane QLD
    </p>
    <div class="rule rule-low"></div>
    <div class="rule rule-base"></div>
    <div class="back-pill"></div>
  </section>
</main>
</body>
</html>
```